Belford & Company

We are a boutique commercial real estate firm. For our Business card design - sleek, modern, yet high-end/classy. Please see our website: belfordandcompany.example for details.

We currently need 2 business card names and the ability to add/change the business card information -
Name, Title, Address, Office #, Mobile #, Fax, Email and company website.

Industry/Entity Type

Real Estate

Contact Information for Business Card

Business card design - sleek, modern, yet high-end/classy. Please see our website: belfordandcompany.example for details.

Also, we'd like to have our slogan "Precision Shapes Every Deal." somewhere in there. We'd like to make some part of it raised or a different texture if possible.
Color #'s:
blue 19 36 128
light gray 222 222 221
dark gray 107 120 128

Also, we'd like to have our slogan "Precision Shapes Every Deal." somewhere in there. We'd like to make some part of it raised or a different texture if possible - grey on one side and blue on the other - rounded edges preferred. Maybe either metal/silver/grey raised logo on the back. Thank you!!

Requirements
Must have
• Sleek, modern, clean and classy design

```html
<!DOCTYPE html>
<html lang="en">
<head>
<meta charset="utf-8">
<title>Belford &amp; Company – Business Card</title>
<link rel="stylesheet" href="https://fonts.googleapis.com/css2?family=Roboto:ital,wght@0,400;0,500;0,700;1,400&display=swap">
<style>
  :root {
    --backdrop: #2a2a2c;
    --card-blue: #1d33a6;
    --card-blue-deep: #132480;
    --silver: #dededd;
    --slate: #6b7880;
    --ink-white: #f4f5fa;
  }
  * { box-sizing: border-box; margin: 0; padding: 0; }
  html, body {
    width: 1200px; height: 1063px; overflow: hidden;
    background: var(--backdrop);
    font-family: "Roboto", Arial, sans-serif;
  }
  .sheet { position: relative; width: 1200px; height: 1063px; }
  .card {
    position: absolute; left: 220px; width: 760px; height: 434px;
    border-radius: 12px;
    background: linear-gradient(135deg, var(--card-blue) 0%, var(--card-blue-deep) 100%);
    color: var(--ink-white);
  }
  .card--back { top: 90px; }
  .card--front { top: 560px; }

  /* back side */
  .back-mark {
    position: absolute; left: 0; right: 0; top: 150px;
    display: flex; flex-direction: column; align-items: center; gap: 18px;
  }
  .back-mark__square { width: 34px; height: 34px; background: var(--silver); }
  .back-mark__name {
    font-weight: 700; font-size: 36px; letter-spacing: 1px; color: var(--silver);
    text-transform: uppercase; white-space: nowrap;
  }
  .slogan {
    position: absolute; left: 0; right: 0; bottom: 44px;
    text-align: center; font-style: italic; font-size: 17px; letter-spacing: 0.5px;
    color: var(--silver);
  }

  /* front side */
  .brand {
    position: absolute; left: 52px; top: 0; bottom: 0; width: 280px;
    display: flex; align-items: center; gap: 16px;
  }
  .brand__square { width: 26px; height: 26px; background: var(--silver); flex: none; }
  .brand__name {
    font-weight: 700; font-size: 30px; line-height: 1.05; color: var(--ink-white);
    text-transform: uppercase;
  }
  .divider {
    position: absolute; left: 352px; top: 70px; bottom: 70px; width: 1px;
    background: rgba(222, 222, 221, 0.55);
  }
  .contact { position: absolute; left: 388px; top: 84px; right: 24px; }
  .contact__name { font-weight: 700; font-size: 24px; letter-spacing: 0.5px; }
  .contact__title { font-weight: 500; font-size: 16px; margin-bottom: 14px; }
  .contact__address { font-size: 15px; line-height: 1.4; margin-bottom: 12px; }
  .contact__list { list-style: none; }
  .contact__item {
    display: flex; align-items: center; gap: 12px; font-size: 15px; line-height: 1.45;
    white-space: nowrap;
  }
  .contact__icon { width: 14px; height: 14px; flex: none; fill: var(--ink-white); }
</style>
</head>
<body>
<main class="sheet">
  <section class="card card--back" aria-label="Card back">
    <div class="back-mark">
      <span class="back-mark__square"></span>
      <span class="back-mark__name">Belford &amp; Company</span>
    </div>
    <p class="slogan">Precision Shapes Every Deal.</p>
  </section>

  <section class="card card--front" aria-label="Card front">
    <div class="brand">
      <span class="brand__square"></span>
      <span class="brand__name">Belford &amp;<br>Company</span>
    </div>
    <div class="divider"></div>
    <div class="contact">
      <p class="contact__name">DANIEL HART</p>
      <p class="contact__title">CEO/FOUNDER</p>
      <p class="contact__address">214 Alder Crest Road<br>Juneau, Alaska 99801</p>
      <ul class="contact__list">
        <li class="contact__item">
          <svg class="contact__icon" viewBox="0 0 24 24"><path d="M6.6 10.8a15.1 15.1 0 0 0 6.6 6.6l2.2-2.2a1 1 0 0 1 1-.25 11.4 11.4 0 0 0 3.6.57 1 1 0 0 1 1 1V20a1 1 0 0 1-1 1A17 17 0 0 1 3 4a1 1 0 0 1 1-1h3.5a1 1 0 0 1 1 1c0 1.250.2 2.45.57 3.57a1 1 0 0 1-.25 1z"/></svg>
          555 014 2297
        </li>
        <li class="contact__item">
          <svg class="contact__icon" viewBox="0 0 24 24"><path d="M7 1h10a2 2 0 0 1 2 2v18a2 2 0 0 1-2 2H7a2 2 0 0 1-2-2V3a2 2 0 0 1 2-2zm0 3v14h10V4zm5 15.2a1.2 1.2 0 1 0 0 2.4 1.2 1.2 0 0 0 0-2.4z"/></svg>
          555 019 4410
        </li>
        <li class="contact__item">
          <svg class="contact__icon" viewBox="0 0 24 24"><path d="M6 2h9l3 3v4H6zM4 10h16a2 2 0 0 1 2 2v7h-4v3H6v-3H2v-7a2 2 0 0 1 2-2zm4 7v3h8v-3z"/></svg>
          555 013 8862
        </li>
        <li class="contact__item">
          <svg class="contact__icon" viewBox="0 0 24 24"><path d="M2 5h20v14H2zm2 2v.5l8 5 8-5V7zm0 2.8V17h16V9.8l-8 5z"/></svg>
          info@belfordandcompany.example
        </li>
        <li class="contact__item">
          <svg class="contact__icon" viewBox="0 0 24 24"><path d="M12 2a10 10 0 1 0 0 20 10 10 0 0 0 0-20zm6.9 9h-3a15 15 0 0 0-1.2-5.6A8 8 0 0 1 18.9 11zM12 4.1c.9 1.2 1.8 3.6 1.9 6.9h-3.8c.1-3.3 1-5.7 1.9-6.9zM9.3 5.4A15 15 0 0 0 8.1 11h-3a8 8 0 0 1 4.2-5.6zM5.1 13h3a15 15 0 0 0 1.2 5.6A8 8 0 0 1 5.1 13zm6.9 6.9c-.9-1.2-1.8-3.6-1.9-6.9h3.8c-.1 3.3-1 5.7-1.9 6.9zm2.7-1.3a15 15 0 0 0 1.2-5.6h3a8 8 0 0 1-4.2 5.6z"/></svg>
          www.belfordandcompany.example
        </li>
      </ul>
    </div>
  </section>
</main>
</body>
</html>
```